Doors for Chiropractic Office

In my chiropractic office I have 6 treatment rooms and 2 massage rooms. The entire office is going through a remodel. The overall color scheme is very earth tones but in order to add some color, the 6 doors to the treatment rooms will all be a separate color (Red, Blue, Yellow, Green etc)
I need to number each room 1,2,3,4,5,6 and the 2 massage rooms. I had the idea of putting a giant number on each door, so I am looking for some graphic ideas for that project.
The rooms are located with 4 on each side of a long hallway with the 2 massage rooms at the end.
The purpose of numbering each door is to direct the patients where to go.
I have uploaded pictures of the hall way. Pardon the dust since we are under construction but hopefully it gives you an idea of the layout. The door colors will change as stated above.

Requirements
Nice to have
• I would like to see someone come up with a design where each number for the doors are created out of vertebrae's.

```html
<!DOCTYPE html>
<html lang="en">
<head>
<meta charset="utf-8">
<title>Treatment Room Door Graphics</title>
<link rel="stylesheet" href="https://fonts.googleapis.com/css2?family=Archivo+Black&display=swap">
<style>
  :root {
    --backdrop: #a7a9ac;
    --frame: #e6e7e8;
    --blue: #1c47a3;   --blue-dark: #17398a;   --blue-num: #2f6cc4;
    --red: #e01f2c;    --red-dark: #b51a24;    --red-num: #f0273a;
    --yellow: #f6d21c; --yellow-dark: #f0ae17; --yellow-num: #faee2e;
    --green: #1c9a43;  --green-dark: #0f7a34;  --green-num: #2db24c;
    --orange: #ec5f1e; --orange-dark: #c7401a; --orange-num: #f5821f;
    --purple: #4a2690; --purple-dark: #2f1866; --purple-num: #6d40b4;
    --wordmark: #ffffff;
  }
  * { box-sizing: border-box; margin: 0; padding: 0; }
  html, body { width: 1200px; height: 374px; overflow: hidden; background: var(--backdrop); }
  .hallway { position: relative; width: 1200px; height: 374px; }
  .door {
    position: absolute; top: 26px; width: 126px; height: 321px;
    background: var(--frame); padding: 5px;
  }
  .door-panel { position: relative; width: 100%; height: 100%; overflow: hidden; }
  .artwork { position: absolute; inset: 0; }
  .room-number {
    position: absolute; left: 29px; top: 37px;
    font-family: "Archivo Black", sans-serif; font-size: 208px; line-height: 1;
    transform: scaleX(0.8); transform-origin: left top;
  }
  .room-1 .door-panel { background: linear-gradient(180deg, var(--blue), var(--blue-dark)); }
  .room-1 .room-number { color: var(--blue-num); left: 27px; }
  .room-2 .door-panel { background: linear-gradient(180deg, var(--red), var(--red-dark)); }
  .room-2 .room-number { color: var(--red-num); left: 27px; }
  .room-3 .door-panel { background: linear-gradient(180deg, var(--yellow), var(--yellow-dark)); }
  .room-3 .room-number { color: var(--yellow-num); }
  .room-4 .door-panel { background: linear-gradient(180deg, var(--green), var(--green-dark)); }
  .room-4 .room-number { color: var(--green-num); left: 25px; }
  .room-5 .door-panel { background: linear-gradient(180deg, var(--orange), var(--orange-dark)); }
  .room-5 .room-number { color: var(--orange-num); left: 25px; }
  .room-6 .door-panel { background: linear-gradient(180deg, var(--purple), var(--purple-dark)); }
  .room-6 .room-number { color: var(--purple-num); left: 23px; }
  .spine-art { background: radial-gradient(ellipse at 30% 40%, rgba(255,255,255,0.08), transparent 60%); }
  .massage-a .artwork { background: linear-gradient(180deg, #9fbccb 0%, #c9d6dc 45%, #b9cfe0 70%, #53657a 100%); }
  .massage-b .artwork { background: linear-gradient(180deg, #a6a35e 0%, #b9a95c 40%, #9c8442 70%, #6f6a3a 100%); }
  .clinic-name {
    position: absolute; left: 12px; right: 8px; top: 34px;
    font-family: "Archivo Black", sans-serif; font-size: 10px; line-height: 1.25;
    color: var(--wordmark);
  }
</style>
</head>
<body>
<main class="hallway">
  <section class="door room-1" style="left:31px"><div class="door-panel">
    <div class="artwork spine-art" role="img" aria-label="Faint vertebrae illustration"></div>
    <span class="room-number">1</span></div></section>
  <section class="door room-2" style="left:174px"><div class="door-panel">
    <div class="artwork spine-art" role="img" aria-label="Faint spine and ribcage illustration"></div>
    <span class="room-number">2</span></div></section>
  <section class="door room-3" style="left:320px"><div class="door-panel">
    <div class="artwork spine-art" role="img" aria-label="Faint vertebrae illustration"></div>
    <span class="room-number">3</span></div></section>
  <section class="door room-4" style="left:464px"><div class="door-panel">
    <div class="artwork spine-art" role="img" aria-label="Faint vertebrae illustration"></div>
    <span class="room-number">4</span></div></section>
  <section class="door room-5" style="left:609px"><div class="door-panel">
    <div class="artwork spine-art" role="img" aria-label="Faint spine and molecule illustration"></div>
    <span class="room-number">5</span></div></section>
  <section class="door room-6" style="left:752px"><div class="door-panel">
    <div class="artwork spine-art" role="img" aria-label="Faint vertebrae illustration"></div>
    <span class="room-number">6</span></div></section>
  <section class="door massage-a" style="left:897px"><div class="door-panel">
    <div class="artwork" role="img" aria-label="Massage photo with candles and lavender"></div>
    <p class="clinic-name">Meadowbrook Chiropractic Massage</p></div></section>
  <section class="door massage-b" style="left:1041px"><div class="door-panel">
    <div class="artwork" role="img" aria-label="Photo of herb jars and dried botanicals"></div>
    <p class="clinic-name">Meadowbrook Chiropractic Massage</p></div></section>
</main>
</body>
</html>
```